Postcard Design

I am a speech pathologist. My company is called Bramble Hop. I have a program called "Quiet Paws" to help children stop sucking their thumb/ fingers. After they complete the program, I need to check in after 6 months to make sure they have continued with their success, and to see if they may be ready for the follow up program "Lark Loops" for those with a tongue thrust.

On one side, I would like "Bramble Hop....Quiet paws to your success!" with my logo. On the other side, I would like a reflective sticker like a mirror that says something like "Bramble hop...it's time to check your smile". Please contact Harriet if you think a Tongue thrust may be present. Lark Loops is a follow up program to retrain the tongue to work properly in the mouth. Please discuss with your orthodontist/ dentist or contact Harriet if you want to schedule an evaluation.
Updates

Reason: Just trying to make sure I get the best postcard as possible. I've extended the deadline by a few days to see what else comes in and to tweak the changes I've already received. Thanks!

Target Market(s)

families and children

Industry/Entity Type

It Company

Requirements
Must have
• logos for Bramble Hop, Quiet Paws, and Lark Loops
Nice to have
• I had this idea of a paper reflective mirror for the back so the children can actually see their smile when they look in it, but know that may be impossible. Just a creative idea.

```html
<!DOCTYPE html>
<html lang="en">
<head>
<meta charset="utf-8">
<title>Bramble Hop Postcards</title>
<link href="https://fonts.googleapis.com/css2?family=Comfortaa:wght@400;600;700&family=Ubuntu:wght@500;700&display=swap" rel="stylesheet">
<style>
:root{
  --bg:#eceae6;
  --white:#ffffff;
  --brand-blue:#3f7dc1;
  --banner-blue:#3b79bd;
  --navy:#2d3b7c;
  --orange:#f0862a;
  --rule:#c9ccd3;
}
*{box-sizing:border-box;margin:0;padding:0}
html,body{width:1200px;height:900px;overflow:hidden;background:var(--bg)}
body{position:relative;font-family:'Comfortaa',sans-serif}
.postcard{position:absolute;background:var(--white);box-shadow:0 4px 14px rgba(0,0,0,.18);overflow:hidden}
.postcard__art{position:absolute;inset:0}
.postcard--back{left:40px;top:30px;width:620px;height:450px}
.postcard--front{left:550px;top:380px;width:610px;height:460px}

.brand-name{position:absolute;font-family:'Comfortaa',sans-serif;font-weight:700;color:var(--brand-blue);letter-spacing:.5px;display:flex;align-items:center;gap:8px;white-space:nowrap}
.brand-dot{display:inline-block;border-radius:50%;background:var(--brand-blue)}
.banner{position:absolute;background:var(--banner-blue);color:var(--white);font-family:'Ubuntu',sans-serif;font-weight:700;white-space:nowrap;box-shadow:2px 2px 4px rgba(0,0,0,.2)}

/* back */
.mirror-tag{position:absolute;left:306px;top:166px;font-family:'Ubuntu',sans-serif;font-weight:700;font-size:14px;color:var(--brand-blue);white-space:nowrap}
.mirror-tag span{color:var(--orange)}
.stamp-box{position:absolute;left:460px;top:15px;width:136px;height:136px;border:1.5px solid var(--rule)}
.address-lines{position:absolute;left:340px;top:220px;width:260px;list-style:none}
.address-lines li{height:1px;background:var(--rule);margin-bottom:38px}
.back-brand{left:20px;top:196px;font-size:24px}
.back-brand .brand-dot{width:11px;height:11px}
.back-banner{left:12px;top:232px;padding:4px 16px;font-size:16px}
.program-name{position:absolute;left:24px;top:266px;font-size:22px;font-weight:600;color:var(--brand-blue);white-space:nowrap}
.program-tagline{position:absolute;left:24px;top:294px;font-size:7px;color:var(--navy);letter-spacing:.3px;white-space:nowrap}
.back-copy{position:absolute;left:24px;top:310px;width:290px;font-size:14px;line-height:19px;color:var(--navy)}

/* front */
.front-brand{left:20px;top:150px;font-size:34px}
.front-brand .brand-dot{width:13px;height:13px}
.front-banner{left:8px;top:203px;width:384px;padding:5px 0 5px 74px;font-size:20px}
.front-copy{position:absolute;left:22px;top:258px;width:290px;font-size:14px;line-height:19px;color:var(--navy)}
.front-copy strong{font-weight:700;color:var(--brand-blue)}
.contact{position:absolute;right:14px;top:404px;list-style:none;color:var(--white);font-size:14px;font-weight:700}
.contact li{display:flex;align-items:center;gap:7px;margin-bottom:5px;white-space:nowrap}
.contact li:first-child{font-size:17px}
.contact svg{flex:none}
</style>
</head>
<body>

<section class="postcard postcard--back" aria-label="Postcard back">
  <svg class="postcard__art" viewBox="0 0 620 450" aria-hidden="true">
    <defs>
      <linearGradient id="backSky" x1="0" y1="0" x2="1" y2="0">
        <stop offset="0" stop-color="#6f92c9"/><stop offset="1" stop-color="#d9e3f3"/>
      </linearGradient>
      <linearGradient id="mirror" x1="0" y1="0" x2="1" y2="0.2">
        <stop offset="0" stop-color="#5d5d5d"/><stop offset=".25" stop-color="#d6d6d6"/>
        <stop offset=".45" stop-color="#6a6a6a"/><stop offset=".7" stop-color="#cfcfcf"/>
        <stop offset="1" stop-color="#5a5a5a"/>
      </linearGradient>
    </defs>
    <path d="M0,0 H450 V158 Q220,150 0,190 Z" fill="url(#backSky)"/>
    <path d="M40,14 H446 V146 Q240,142 40,176 Z" fill="url(#mirror)"/>
    <path d="M0,70 Q220,10 446,8" fill="none" stroke="#3b6fb4" stroke-width="3"/>
    <path d="M0,190 Q220,148 450,158" fill="none" stroke="#3b6fb4" stroke-width="2"/>
  </svg>
  <div class="stamp-box"></div>
  <p class="mirror-tag"><span>chech</span> your smile!!</p>
  <p class="brand-name back-brand"><span class="brand-dot"></span>Bramble hop</p>
  <p class="banner back-banner">it's time to check your smile</p>
  <p class="program-name">Lark Loops</p>
  <p class="program-tagline">A TONGUE THRUST REMEDIATION PROGRAM</p>
  <p class="back-copy">Lark Loops is a follow up program to retrain the tongue to work properly in the mouth. Please discuss with your orthodontist/ dentist or contact Harriet if you want to schedule an evaluation.</p>
  <ul class="address-lines"><li></li><li></li><li></li><li></li></ul>
</section>

<section class="postcard postcard--front" aria-label="Postcard front">
  <svg class="postcard__art" viewBox="0 0 610 460">
    <defs>
      <linearGradient id="frontSky" x1="0" y1="0" x2="0" y2="1">
        <stop offset="0" stop-color="#8ea9d8"/><stop offset="1" stop-color="#e6ecf6"/>
      </linearGradient>
      <linearGradient id="photoTone" x1="0" y1="0" x2="1" y2="1">
        <stop offset="0" stop-color="#d9d4d0"/><stop offset=".45" stop-color="#a7755a"/>
        <stop offset=".75" stop-color="#7a4a33"/><stop offset="1" stop-color="#b23a3a"/>
      </linearGradient>
      <linearGradient id="footBand" x1="0" y1="0" x2="1" y2="0">
        <stop offset="0" stop-color="#c9d6ee"/><stop offset="1" stop-color="#6f8fcb"/>
      </linearGradient>
    </defs>
    <rect width="610" height="460" fill="url(#frontSky)" aria-hidden="true"/>
    <path role="img" aria-label="Photo of a smiling young child in a classroom" d="M250,90 Q430,32 610,12 V300 Q470,400 320,440 L320,200 Z" fill="url(#photoTone)"/>
    <rect x="0" y="246" width="320" height="200" fill="#ffffff" opacity=".85" aria-hidden="true"/>
    <path d="M0,448 Q360,448 610,300 V460 H0 Z" fill="url(#footBand)" aria-hidden="true"/>
    <path d="M0,150 Q300,40 610,18" fill="none" stroke="#ffffff" stroke-width="3" aria-hidden="true"/>
    <path d="M0,160 Q300,52 610,28" fill="none" stroke="#3b6fb4" stroke-width="2" aria-hidden="true"/>
    <path d="M0,448 Q360,448 610,300" fill="none" stroke="#ffffff" stroke-width="3" aria-hidden="true"/>
  </svg>
  <p class="brand-name front-brand"><span class="brand-dot"></span>Bramble Hop</p>
  <p class="banner front-banner">Quiet paws to your success!</p>
  <p class="front-copy"><strong>Quiet Paws!</strong> is a program that helps children stop sucking their thumb/ fingers. After 6 months a check is made to make sure they have continued with their success, and to see if they may be ready for the follow up program "Lark Loops" for those with a tongue thrust.</p>
  <ul class="contact">
    <li><svg width="14" height="14" viewBox="0 0 24 24" aria-hidden="true"><path d="M6.6 10.8a15 15 0 0 0 6.6 6.6l2.2-2.2a1 1 0 0 1 1-.25 11.4 11.4 0 0 0 3.6.57 1 1 0 0 1 1 1V20a1 1 0 0 1-1 1A17 17 0 0 1 3 4a1 1 0 0 1 1-1h3.5a1 1 0 0 1 1 1c0 1.25.2 2.45.57 3.57a1 1 0 0 1-.25 1Z" fill="#f0862a"/></svg>555-014-2237</li>
    <li><svg width="15" height="12" viewBox="0 0 24 18" aria-hidden="true"><rect x="1" y="1" width="22" height="16" rx="1" fill="none" stroke="#f0862a" stroke-width="2"/><path d="M1 2l11 8 11-8" fill="none" stroke="#f0862a" stroke-width="2"/></svg>hello@bramblehop.example</li>
  </ul>
</section>

</body>
</html>
```